v-orn design for startup inpection service

building and pest inspections what i had in mind was v-orn in large print with prepurchase in small print directly under it and the small tm (tradmark) .Within the C I would like an eye but I don't want to take away from the C so maybe the eye would be done in a fine line?I would also like the Building and Pest inspections to be prominent and large .Have no idea of colors but do like black orange and silver

Target Market(s)

home buyers and realestate agents

Industry/Entity Type

Building

Contact Information for Business Card

v-orn prepurchase, Phone 0417382951, fax 02 93147708, email v-orn@mailbay.com.au ,building and pest inspections

Font styles to use
Sans Serif

Requirements
Must have
• bold color
• simple layout
• bold color
• uncluttered layout
Should not have
• contact details the same size as Building and Pest Inspections

```html
<!DOCTYPE html>
<html lang="en">
<head>
<meta charset="utf-8">
<title>V-orn Prepurchase – Business Card</title>
<link href="https://fonts.googleapis.com/css2?family=Orbitron:wght@800&family=Exo+2:wght@600&display=swap" rel="stylesheet">
<style>
  :root {
    --backdrop: #2a2a2a;
    --card-white: #f7f7f7;
    --lime: #c6f000;
    --charcoal: #2e2e2e;
    --ink: #1f1f1f;
  }
  * { margin: 0; padding: 0; box-sizing: border-box; }
  html, body {
    width: 1200px;
    height: 848px;
    overflow: hidden;
    background: var(--backdrop);
  }
  .business-card {
    position: absolute;
    left: 100px;
    top: 134px;
    width: 1000px;
    height: 580px;
    background: var(--card-white);
    overflow: hidden;
  }
  .card-accent {
    position: absolute;
    left: 0;
    top: 0;
    width: 1000px;
    height: 450px;
  }
  .business-name {
    position: absolute;
    left: 60px;
    top: 90px;
    font-family: "Exo 2", sans-serif;
    font-weight: 600;
    font-size: 48px;
    line-height: 1.1;
    color: var(--ink);
  }
  .contact-list {
    position: absolute;
    right: 70px;
    top: 180px;
    list-style: none;
    text-align: right;
    font-family: "Exo 2", sans-serif;
    font-weight: 600;
    font-size: 29px;
    line-height: 1.45;
    color: var(--ink);
  }
  .service-band {
    position: absolute;
    left: 0;
    bottom: 0;
    width: 1000px;
    height: 130px;
    background: var(--charcoal);
    display: flex;
    align-items: center;
    justify-content: center;
  }
  .service-title {
    font-family: "Orbitron", sans-serif;
    font-weight: 800;
    font-size: 42px;
    letter-spacing: 3px;
    color: var(--lime);
    text-transform: uppercase;
    white-space: nowrap;
  }
</style>
</head>
<body>
  <article class="business-card">
    <svg class="card-accent" viewBox="0 0 1000 450" aria-hidden="true">
      <polygon points="575,0 1000,0 1000,450 395,450" fill="var(--lime)"/>
    </svg>

    <p class="business-name">V-orn Prepurchase</p>

    <ul class="contact-list">
      <li>Phone 0417382951</li>
      <li>Fax 02 93147708</li>
      <li>Email v-orn@mailbay.com.au</li>
    </ul>

    <footer class="service-band">
      <h1 class="service-title">Building and Pest Inspections</h1>
    </footer>
  </article>
</body>
</html>
```